Aunt Rolina's Bakery

I am about to create a luxury boutique that specializes in cake baking and cupcake
and ready for parties and special events and order delivery
the logo has already made

Industry/Entity Type

Boutique

Contact Information for Business Card

Email:auntrolinasbakery@maplecrumbmail.com
Instagram: aunt_rolina_bakery
Twitter: xxxxxxx
WhatsApp: xxxxxxx

Requirements
Must have
• luxury design

```html
<!DOCTYPE html>
<html lang="en">
<head>
<meta charset="utf-8">
<title>Aunt Rolina's Bakery – Business Card</title>
<link href="https://fonts.googleapis.com/css2?family=Source+Sans+3:wght@400;600&display=swap" rel="stylesheet">
<style>
  :root {
    --backdrop: #ece9e4;
    --card: #ffffff;
    --slate: #7a7a77;
    --rose: #e4a2b3;
    --rose-deep: #d98aa0;
    --ink: #3a3a3a;
    --on-slate: #ffffff;
  }
  * { margin: 0; padding: 0; box-sizing: border-box; }
  html, body {
    width: 1200px; height: 902px; overflow: hidden;
    background: var(--backdrop);
    font-family: "Source Sans 3", sans-serif;
  }
  .canvas { position: relative; width: 1200px; height: 902px; }
  .business-card {
    position: absolute; left: 100px; top: 165px;
    width: 1000px; height: 571px;
    background: var(--card);
    overflow: hidden;
    box-shadow: 0 8px 28px rgba(0,0,0,0.12);
  }
  .card-wave { position: absolute; inset: 0; width: 100%; height: 100%; }
  .holder {
    position: absolute; left: 560px; top: 62px;
  }
  .holder-company {
    font-size: 30px; font-weight: 600; color: var(--rose-deep);
    line-height: 1.1;
  }
  .holder-role {
    font-size: 22px; color: var(--ink); margin-top: 4px; margin-left: 24px;
  }
  .brand {
    position: absolute; left: 120px; top: 230px; width: 380px;
    text-align: center;
  }
  .brand-dot {
    width: 64px; height: 64px; border-radius: 50%;
    background: var(--rose); margin: 0 auto 14px;
  }
  .brand-name {
    font-size: 40px; font-weight: 400; color: var(--slate);
    letter-spacing: 1px; line-height: 1.1;
  }
  .contact {
    position: absolute; left: 665px; top: 300px;
    width: 320px;
    list-style: none; color: var(--on-slate); font-size: 18px;
  }
  .contact-item { display: flex; align-items: center; gap: 10px; height: 36px; white-space: nowrap; }
  .contact-icon { width: 18px; height: 18px; flex: none; display: flex; align-items: center; justify-content: center; font-weight: 600; }
  .contact-icon svg { width: 16px; height: 16px; fill: var(--on-slate); }
  .contact-email { font-size: 16px; }
</style>
</head>
<body>
<main class="canvas">
  <section class="business-card">
    <svg class="card-wave" viewBox="0 0 1000 571" preserveAspectRatio="none" aria-hidden="true">
      <path fill="var(--slate)" d="M1000,92 C860,86 748,128 680,210 C760,140 870,112 1000,112 Z"/>
      <path fill="var(--slate)" d="M1000,122 C830,122 720,180 640,290 C560,400 420,505 0,522 L0,571 L1000,571 Z"/>
      <path fill="var(--card)" d="M760,150 C680,200 630,300 560,380 C500,450 430,500 330,530 C450,510 540,460 600,390 C660,310 700,210 760,150 Z"/>
    </svg>

    <div class="holder">
      <p class="holder-company">Aunt Rolina bakery</p>
      <p class="holder-role">Manager</p>
    </div>

    <div class="brand">
      <div class="brand-dot"></div>
      <p class="brand-name">Aunt Rolina's Bakery</p>
    </div>

    <ul class="contact">
      <li class="contact-item">
        <span class="contact-icon">
          <svg viewBox="0 0 24 24"><path d="M6.6 10.8a15.1 15.1 0 0 0 6.6 6.6l2.2-2.2a1 1 0 0 1 1-.25 11.4 11.4 0 0 0 3.6.57 1 1 0 0 1 1 1V20a1 1 0 0 1-1 1A17 17 0 0 1 3 4a1 1 0 0 1 1-1h3.5a1 1 0 0 1 1 1c0 1.250.2 2.45.57 3.6a1 1 0 0 1-.25 1z"/></svg>
        </span>
        <span>123 456 7890</span>
      </li>
      <li class="contact-item">
        <span class="contact-icon">
          <svg viewBox="0 0 24 24"><circle cx="12" cy="12" r="6"/></svg>
        </span>
        <span>xxx xxx xxx</span>
      </li>
      <li class="contact-item">
        <span class="contact-icon">@</span>
        <span class="contact-email">auntrolinasbakery@maplecrumbmail.com</span>
      </li>
    </ul>
  </section>
</main>
</body>
</html>
```